Owen Tasker Studios Business Card

Looking for a clear, modern, elegant, sharp business card that conveys a professional yet edgy image to my business as a wedding, portrait, and travel photographer. Would like something that looks vintage yet modern. Need a new business card to grow my business. We are growing the business for Wedding and Event Photography as well as fine art Photography. (Mostly Landscapes)
Updates

I’m looking through designs now but I have a new logo that i want using please.

New logo uploaded please redesign using that

PLEASE ALL DESIGNERS LOOK IN BRIEF FOR NEW LOGO

Target Market(s)

Brides, Grooms, Families with Kids, People looking for Fine Art Photography Artwork

Industry/Entity Type

Photographer

Contact Information for Business Card

Unsure

Font styles to use
Serif

Colors

Designer to choose colors to be used in the design.

Requirements
Must have
• My Website:
• http://taskerlens.examplefolio.net
• Phone:
• 323-481-5206
• Email:
• owentaskerlens@mailbox-example.net
Nice to have
• Would like a sort of shine on the printing finish.
• I like black I think it looks good on a business card.
• Can try working with my logo (png that I've attached)

```html
<!DOCTYPE html>
<html lang="en">
<head>
<meta charset="utf-8">
<title>Owen Tasker Studios Business Card</title>
<link href="https://fonts.googleapis.com/css2?family=Lato:wght@300;400&family=Oswald:wght@600&display=swap" rel="stylesheet">
<style>
  :root {
    --backdrop: #161616;
    --card: #1c1c1d;
    --card-edge: #262627;
    --mark-grey: #8a8a8c;
    --text-grey: #6f6f72;
    --text-light: #f2f2f2;
    --text-soft: #d6d6d6;
  }
  * { margin: 0; padding: 0; box-sizing: border-box; }
  html, body { width: 1200px; height: 896px; overflow: hidden; }
  body {
    background: var(--backdrop);
    font-family: "Lato", sans-serif;
    position: relative;
  }
  .card {
    position: absolute;
    left: 357px;
    width: 486px;
    height: 276px;
    background: var(--card);
    border-radius: 16px;
    border: 1px solid var(--card-edge);
    box-shadow: 0 8px 24px rgba(0,0,0,0.55);
  }
  .card--front { top: 162px; }
  .card--back { top: 469px; }

  /* Front */
  .front-mark {
    position: absolute;
    left: 214px; top: 77px;
    width: 58px; height: 58px;
    border: 1px solid var(--mark-grey);
  }
  .front-name {
    position: absolute;
    left: 0; right: 0; top: 148px;
    text-align: center;
    font-weight: 300;
    font-size: 28px;
    letter-spacing: 1px;
    color: var(--mark-grey);
  }
  .front-studio {
    position: absolute;
    left: 0; right: 0; top: 186px;
    text-align: center;
    font-weight: 300;
    font-size: 13px;
    letter-spacing: 7px;
    padding-left: 7px;
    color: var(--mark-grey);
  }
  .front-web {
    position: absolute;
    left: 0; right: 0; top: 234px;
    text-align: center;
    font-size: 11px;
    letter-spacing: 0.8px;
    color: var(--text-grey);
  }

  /* Back */
  .back-brand {
    position: absolute;
    right: 24px; top: 22px;
    display: flex; align-items: center; gap: 8px;
  }
  .back-brand__name {
    font-size: 10px;
    letter-spacing: 1.5px;
    color: var(--text-soft);
  }
  .back-brand__square {
    width: 40px; height: 40px;
    border: 1px solid var(--text-soft);
  }
  .identity {
    position: absolute;
    right: 258px; top: 112px;
    text-align: right;
  }
  .identity__name {
    font-family: "Oswald", sans-serif;
    font-weight: 600;
    font-size: 23px;
    line-height: 1.1;
    color: var(--text-light);
  }
  .identity__role {
    font-size: 11px;
    color: var(--text-soft);
  }
  .divider {
    position: absolute;
    left: 236px; top: 114px;
    width: 1px; height: 44px;
    background: var(--text-soft);
  }
  .contacts {
    position: absolute;
    left: 244px; top: 114px;
    list-style: none;
  }
  .contacts li {
    display: flex; align-items: center; gap: 6px;
    font-size: 10.5px;
    line-height: 15px;
    color: var(--text-light);
    white-space: nowrap;
  }
  .contacts svg { width: 8px; height: 8px; fill: var(--text-light); flex: none; }
</style>
</head>
<body>
  <section class="card card--front">
    <div class="front-mark"></div>
    <div class="front-name">OWEN TASKER</div>
    <div class="front-studio">STUDIOS</div>
    <div class="front-web">taskerlens.examplefolio.net</div>
  </section>

  <section class="card card--back">
    <div class="back-brand">
      <span class="back-brand__name">OWEN TASKER</span>
      <span class="back-brand__square"></span>
    </div>
    <div class="identity">
      <div class="identity__name">OWEN TASKER</div>
      <div class="identity__role">Director</div>
    </div>
    <div class="divider"></div>
    <ul class="contacts">
      <li>
        <svg viewBox="0 0 10 10"><path d="M2 0.5 L3.6 2.6 L2.8 3.6 C3.5 5 5 6.5 6.4 7.2 L7.4 6.4 L9.5 8 L8.4 9.5 C4.5 9.5 0.5 5.5 0.5 1.6 Z"/></svg>
        323-481-5206
      </li>
      <li>
        <svg viewBox="0 0 10 10"><path d="M0.5 2 H9.5 V8.5 H0.5 Z M1 2.4 L5 5.6 L9 2.4" fill="none" stroke="#f2f2f2" stroke-width="1"/></svg>
        owentaskerlens@mailbox-example.net
      </li>
      <li>
        <svg viewBox="0 0 10 10"><circle cx="6" cy="4" r="3" fill="none" stroke="#f2f2f2" stroke-width="1.3"/><path d="M3.9 6.1 L0.8 9.2" stroke="#f2f2f2" stroke-width="1.5"/></svg>
        taskerlens.examplefolio.net
      </li>
    </ul>
  </section>
</body>
</html>
```